Need innovative card design for tech start up

We are a Santa Monica based marketing analytics software start up called Brightwell Metrics. We're launching a platform that will help advertisers better measure and optimize their marketing spend by using advanced algorithmic analytic. While our subject matter is complicated, we want to convey simple, clean, curated. We also want to stand out - ad tech is a sea of sameness and we need to have some individuality. We have an established color palette and would like to see a design we could print in each tone (teal, tangerine, grey), but it doesn't require the card to be monochromatic. The font used is DENSE.

Marketing

```html
<!DOCTYPE html>
<html lang="en">
<head>
<meta charset="utf-8">
<title>Brightwell Metrics — Business Cards</title>
<link rel="stylesheet" href="https://fonts.googleapis.com/css2?family=Oswald:wght@300;400&family=Open+Sans:wght@400;600&display=swap">
<style>
  :root {
    --backdrop: #e6e7e9;
    --card-white: #ffffff;
    --card-blue: #5aade3;
    --ink: #2f3133;
    --ink-soft: #55585c;
    --rule: #b9bcc0;
    --faint-grey: #d8dadd;
    --faint-blue: #b7dbf3;
    --brand-white: #ffffff;
  }
  * { box-sizing: border-box; margin: 0; padding: 0; }
  html, body { width: 1200px; height: 873px; overflow: hidden; }
  body {
    background: var(--backdrop);
    display: flex;
    align-items: center;
    justify-content: center;
    gap: 60px;
  }
  .card {
    width: 520px;
    height: 297px;
    position: relative;
    overflow: hidden;
    box-shadow: 0 6px 18px rgba(0,0,0,0.12);
  }

  /* Contact side */
  .card--contact { background: var(--card-white); }
  .contact-brand {
    position: absolute;
    left: 36px; top: 34px;
    display: flex; align-items: center; gap: 10px;
  }
  .contact-brand__square {
    width: 22px; height: 22px;
    background: var(--rule);
  }
  .contact-brand__name {
    font-family: "Oswald", sans-serif;
    font-weight: 300;
    font-size: 22px;
    letter-spacing: 1px;
    text-transform: uppercase;
    color: var(--rule);
  }
  .contact-rule {
    position: absolute;
    left: 36px; top: 86px;
    width: 250px; height: 1px;
    background: var(--rule);
  }
  .contact-details {
    position: absolute;
    left: 36px; top: 100px;
    font-family: "Open Sans", sans-serif;
    color: var(--ink);
  }
  .contact-details__name { font-size: 18px; font-weight: 400; line-height: 1.15; }
  .contact-details__role {
    font-size: 9px; color: var(--ink-soft); margin-bottom: 14px;
  }
  .contact-details__line { font-size: 13px; line-height: 1.3; }
  .contact-details__email { margin-top: 8px; font-size: 13px; }

  .brand-echo {
    position: absolute;
    right: 28px; top: 24px;
    display: flex; flex-direction: column; gap: 30px;
    text-align: right;
  }
  .brand-echo__line {
    font-family: "Oswald", sans-serif;
    font-weight: 300;
    font-size: 17px;
    letter-spacing: 1px;
    text-transform: uppercase;
    color: var(--faint-grey);
  }
  .brand-echo__line--blue { color: var(--faint-blue); }

  /* Brand side */
  .card--brand { background: var(--card-blue); }
  .brand-lockup {
    position: absolute;
    left: 44px; top: 110px;
    display: flex; align-items: center; gap: 14px;
  }
  .brand-lockup__square {
    width: 34px; height: 34px;
    background: var(--brand-white);
  }
  .brand-lockup__name {
    font-family: "Oswald", sans-serif;
    font-weight: 300;
    font-size: 40px;
    letter-spacing: 1px;
    text-transform: uppercase;
    color: var(--brand-white);
    line-height: 1;
  }
  .brand-web {
    position: absolute;
    left: 92px; top: 170px;
    font-family: "Open Sans", sans-serif;
    font-weight: 600;
    font-size: 13px;
    letter-spacing: 2px;
    color: var(--ink);
  }
</style>
</head>
<body>
  <section class="card card--contact" aria-label="Business card, contact side">
    <div class="contact-brand">
      <span class="contact-brand__square"></span>
      <span class="contact-brand__name">Brightwell Metrics</span>
    </div>
    <div class="contact-rule"></div>
    <div class="contact-details">
      <p class="contact-details__name">Owen Hartley</p>
      <p class="contact-details__role">Founder/CEO</p>
      <p class="contact-details__line">1180 Harbor Crest, suite 410</p>
      <p class="contact-details__line">Cedar Falls, OR 97520</p>
      <p class="contact-details__line">Off: 541-555-0142 x220</p>
      <p class="contact-details__line">Mob: 541-555-0187</p>
      <p class="contact-details__email">owen@brightwellmetrics.com</p>
    </div>
    <div class="brand-echo" aria-hidden="true">
      <span class="brand-echo__line">Brightwell Metrics</span>
      <span class="brand-echo__line brand-echo__line--blue">Brightwell Metrics</span>
      <span class="brand-echo__line">Brightwell Metrics</span>
      <span class="brand-echo__line brand-echo__line--blue">Brightwell Metrics</span>
    </div>
  </section>

  <section class="card card--brand" aria-label="Business card, brand side">
    <div class="brand-lockup">
      <span class="brand-lockup__square"></span>
      <span class="brand-lockup__name">Brightwell Metrics</span>
    </div>
    <p class="brand-web">www.brightwellmetrics.com</p>
  </section>
</body>
</html>
```